BuildLinkHub.com Full Stationery Design

Business Card will have all info on it. Letterhead will not have name, title or mobile number. Keep general feeling very clean, using colors from the logo as accents.
Name:Dale Morrisette
Title:President
Phone: 1-800-555-0142
Cell: 306-555-0179
email: dale@buildlinkhub.example
website: www.buildlinkhub.example
Address:
PO Box 872
Harlow Creek, MB
S0J2T0

Target Market(s)

Construction Business owners

Industry/Entity Type

Business

Contact Information for Business Card

Name:Dale Morrisette
Title:President
Phone: 1-800-555-0142
Cell: 306-555-0179
Address:
PO Box 872
Harlow Creek, MB
S0J2T0

Font styles to use
Sans Serif

Requirements
Must have
• Clean look
Should not have
• Images or cartoon type characters or tools

```html
<!DOCTYPE html>
<html lang="en">
<head>
<meta charset="utf-8">
<title>BuildLinkHub.com Letterhead</title>
<link href="https://fonts.googleapis.com/css2?family=Roboto+Condensed:wght@400&family=Montserrat:wght@600&display=swap" rel="stylesheet">
<style>
  :root {
    --backdrop: #efe6e3;
    --paper: #ffffff;
    --accent-orange: #e8501c;
    --slate: #5b636c;
    --steel: #8c98a5;
    --steel-dark: #6f7b88;
  }
  * { box-sizing: border-box; margin: 0; padding: 0; }
  html, body {
    width: 1200px; height: 784px; overflow: hidden;
    background: var(--backdrop);
  }
  .letterhead {
    position: absolute; left: 340px; top: 24px;
    width: 520px; height: 736px;
    background: var(--paper);
    box-shadow: 0 2px 10px rgba(0,0,0,0.08);
  }
  .corner-mark {
    position: absolute; top: 0; height: 4px; display: flex; gap: 4px;
  }
  .corner-mark--left { left: 0; }
  .corner-mark--right { right: 0; }
  .corner-mark span { display: block; width: 16px; height: 4px; }
  .corner-mark .mark-steel { background: var(--steel); }
  .corner-mark .mark-orange { background: var(--accent-orange); }

  .brand {
    position: absolute; top: 78px; right: 40px;
    display: flex; align-items: center; gap: 8px;
  }
  .brand-square { width: 18px; height: 18px; background: var(--accent-orange); }
  .brand-name {
    font-family: "Montserrat", sans-serif; font-weight: 600;
    font-size: 17px; color: var(--slate); letter-spacing: 0.2px;
  }

  .footer-band {
    position: absolute; left: 0; right: 0; bottom: 0; height: 20px;
    display: flex; align-items: stretch;
  }
  .contact-strip {
    flex: 0 0 450px; background: var(--accent-orange);
    display: flex; align-items: center; gap: 8px; padding: 0 8px 0 10px;
    font-family: "Roboto Condensed", sans-serif; font-size: 8.5px; color: #fff;
    white-space: nowrap; overflow: hidden;
  }
  .contact-item { display: flex; align-items: center; gap: 3px; }
  .contact-item svg { width: 8px; height: 8px; flex: 0 0 8px; }
  .band-square {
    flex: 0 0 20px; display: flex; align-items: center; justify-content: center;
  }
  .band-square span { width: 12px; height: 12px; background: var(--steel-dark); }
  .steel-strip {
    flex: 1; background: linear-gradient(180deg, var(--steel) 0%, var(--steel-dark) 100%);
  }
</style>
</head>
<body>
  <main class="letterhead">
    <div class="corner-mark corner-mark--left"><span class="mark-steel"></span><span class="mark-orange"></span></div>
    <div class="corner-mark corner-mark--right"><span class="mark-steel"></span><span class="mark-orange"></span></div>

    <header class="brand">
      <span class="brand-square"></span>
      <span class="brand-name">BuildLinkHub.com</span>
    </header>

    <footer class="footer-band">
      <div class="contact-strip">
        <span class="contact-item">
          <svg viewBox="0 0 10 10"><path d="M5 0.5a3 3 0 0 0-3 3c0 2.3 3 6 3 6s3-3.7 3-6a3 3 0 0 0-3-3z" fill="#fff"/></svg>
          PO Box 872, Harlow Creek, MB S0J2T0
        </span>
        <span class="contact-item">
          <svg viewBox="0 0 10 10"><circle cx="5" cy="5" r="4.5" fill="#fff"/></svg>
          1-800-555-0142
        </span>
        <span class="contact-item">
          <svg viewBox="0 0 10 10"><circle cx="5" cy="5" r="4.5" fill="#fff"/></svg>
          dale@buildlinkhub.example
        </span>
        <span class="contact-item">
          <svg viewBox="0 0 10 10"><circle cx="5" cy="5" r="4.5" fill="#fff"/></svg>
          www.buildlinkhub.example
        </span>
      </div>
      <div class="band-square"><span></span></div>
      <div class="steel-strip"></div>
    </footer>
  </main>
</body>
</html>
```